Husband and i just started a new Hotshot trucking company, Its a pick up and delivery service. We own our own 40 foot gooseneck trailer... Called Roadbird Hauling LLC. We are needing some business cards made to help advertise our new company. We are based out of Ft Worth Tx. We are the ones who transports what ever loads to where ever they need to go, at any time. We stride for success. And we wont take no for an answer.
What we need on there is the following: need it to be all caps please.

DOUGLAS PRATHER "BO"
555-318-4426
ROADBIRDHAULINGLLC@MAILNEST.EXAMPLE

SHELBY CORWIN
555-604-7153

We have a couple logos already made. however we are always game to see new ideas. Thank you for your time.

Target Market(s)

Youth, middle aged. Home buyers

Industry/Entity Type

Hotshot Trucking Pick up and Delivery Service

Contact Information for Business Card

DOUGLAS PRATHER "BO" 555-318-4426 ROADBIRDHAULINGLLC@MAILNEST.EXAMPLE SHELBY CORWIN 555-604-7153 ROADBIRDHAULINGLLC@MAILNEST.EXAMPLE

Font styles to use
Serif
Script

Colors
0054AA
0677BA
7BADD7
CADEEF
E8F1F8
0094D4
00A9DD
6FCCEA
C7EBF8
E9F6FB

Requirements
Must have
• Our company logo. and look one of a kind. also has to be able to catch some ones eye and stand out
Nice to have
• open for ideas..

```html
<!DOCTYPE html>
<html lang="en">
<head>
<meta charset="utf-8">
<title>Roadbird Hauling LLC – Business Card</title>
<link rel="stylesheet" href="https://fonts.googleapis.com/css2?family=Almendra+SC&family=Noto+Serif:wght@400&display=swap">
<style>
  :root {
    --page: #e4e2de;
    --card: #f4f1ec;
    --card-edge: #ffffff;
    --teal: #1c9ea5;
    --teal-bar: #2aa6ab;
    --ink: #1b8f99;
  }
  html, body {
    margin: 0;
    padding: 0;
    width: 1200px;
    height: 1047px;
    overflow: hidden;
    background: var(--page);
  }
  .card {
    position: absolute;
    left: 60px;
    top: 230px;
    width: 1080px;
    height: 588px;
    background: var(--card);
    border: 2px solid var(--card-edge);
    border-radius: 26px;
    box-sizing: border-box;
    box-shadow: 0 10px 30px rgba(0,0,0,0.12);
  }
  .edge-bar {
    position: absolute;
    background: var(--teal-bar);
  }
  .edge-bar--left  { left: 0;  top: 103px; width: 46px; height: 450px; }
  .edge-bar--right { left: 1041px; top: 109px; width: 35px; height: 442px; }
  .divider {
    position: absolute;
    left: 523px;
    top: 106px;
    width: 3px;
    height: 374px;
    background: var(--teal);
  }
  .brand {
    position: absolute;
    left: 60px;
    top: 143px;
    width: 438px;
    height: 300px;
    display: flex;
    flex-direction: column;
    align-items: center;
    justify-content: center;
    gap: 14px;
    font-family: "Almendra SC", "Noto Serif", serif;
    color: var(--teal);
    text-align: center;
  }
  .brand__mark {
    width: 54px;
    height: 54px;
    border-radius: 50%;
    background: var(--teal);
  }
  .brand__name {
    font-size: 44px;
    line-height: 1.1;
    margin: 0;
    font-weight: 400;
  }
  .contacts {
    position: absolute;
    left: 556px;
    top: 110px;
    width: 500px;
  }
  .person { margin: 0; }
  .person + .person { margin-top: 106px; }
  .person__name {
    font-family: "Almendra SC", "Noto Serif", serif;
    font-size: 33px;
    font-weight: 400;
    color: var(--teal);
    margin: 0 0 22px;
    letter-spacing: 0.5px;
    white-space: nowrap;
  }
  .person__line {
    display: flex;
    align-items: center;
    gap: 10px;
    font-family: "Noto Serif", serif;
    color: var(--ink);
    margin: 0 0 12px;
    white-space: nowrap;
  }
  .person__line--phone { font-size: 24px; }
  .person__line--mail  { font-size: 17.5px; }
  .icon { width: 22px; height: 22px; flex: none; fill: var(--ink); }
</style>
</head>
<body>
  <div class="card">
    <div class="edge-bar edge-bar--left"></div>
    <div class="edge-bar edge-bar--right"></div>

    <div class="brand">
      <div class="brand__mark"></div>
      <p class="brand__name">ROADBIRD<br>HAULING LLC</p>
    </div>

    <div class="divider"></div>

    <div class="contacts">
      <div class="person">
        <h2 class="person__name">DOUGLAS PRATHER "BO"</h2>
        <p class="person__line person__line--phone">
          <svg class="icon" viewBox="0 0 24 24" aria-hidden="true"><path d="M2 9c0-3 5-5 10-5s10 2 10 5v2h-5V9c-2-1-8-1-10 0v2H2zM5 13h14l2 7H3z"/></svg>
          555-318-4426
        </p>
        <p class="person__line person__line--mail">
          <svg class="icon" viewBox="0 0 24 24" aria-hidden="true"><path d="M2 5h20v2l-10 6L2 7zM2 9l10 6 10-6v10H2z"/></svg>
          ROADBIRDHAULINGLLC@MAILNEST.EXAMPLE
        </p>
      </div>
      <div class="person">
        <h2 class="person__name">SHELBY CORWIN</h2>
        <p class="person__line person__line--phone">
          <svg class="icon" viewBox="0 0 24 24" aria-hidden="true"><path d="M2 9c0-3 5-5 10-5s10 2 10 5v2h-5V9c-2-1-8-1-10 0v2H2zM5 13h14l2 7H3z"/></svg>
          555-604-7153
        </p>
        <p class="person__line person__line--mail">
          <svg class="icon" viewBox="0 0 24 24" aria-hidden="true"><path d="M2 5h20v2l-10 6L2 7zM2 9l10 6 10-6v10H2z"/></svg>
          ROADBIRDHAULINGLLC@MAILNEST.EXAMPLE
        </p>
      </div>
    </div>
  </div>
</body>
</html>
```